Business Card Design Project

Need a business card with logo that is attached.
Company name: Moberly Swift Solutions, LLC
My name: Lucia Pembrook
Title: President
Phone number: 703-482-1947
Email: lpembrook@moberlyswiftsolutions.example
web site: www.moberlyswiftsolutions.example

Industry/Entity Type

Business

```html
<!DOCTYPE html>
<html lang="en">
<head>
<meta charset="utf-8">
<title>Moberly Swift Solutions, LLC – Business Card</title>
<link rel="stylesheet" href="https://fonts.googleapis.com/css2?family=Tinos&family=Almendra:wght@400;700&display=swap">
<style>
  :root {
    --card-teal: #00745f;
    --card-teal-light: #0a8068;
    --card-teal-dark: #11624f;
    --emblem-fill: #45403d;
    --emblem-edge: #141414;
    --text-light: #ffffff;
    --text-dark: #161616;
    --text-title: #5b3f38;
  }
  html, body {
    margin: 0;
    padding: 0;
    width: 690px;
    height: 1200px;
    overflow: hidden;
    background: var(--card-teal);
  }
  .card {
    position: relative;
    width: 690px;
    height: 1200px;
    overflow: hidden;
    background:
      radial-gradient(ellipse 62% 48% at 50% 30%, var(--card-teal-light) 0%, var(--card-teal) 70%),
      var(--card-teal);
  }
  .card__base-band {
    position: absolute;
    left: 0;
    right: 0;
    bottom: 0;
    height: 110px;
    background: linear-gradient(to bottom, rgba(17, 98, 79, 0) 0%, var(--card-teal-dark) 100%);
  }
  .brand-mark {
    position: absolute;
    left: 175px;
    top: 157px;
    width: 342px;
    height: 342px;
    border-radius: 50%;
    background: var(--emblem-fill);
    border: 2px solid var(--emblem-edge);
    box-sizing: border-box;
    display: flex;
    align-items: center;
    justify-content: center;
    text-align: center;
  }
  .brand-mark__name {
    font-family: "Tinos", "Times New Roman", serif;
    font-size: 31px;
    line-height: 1.25;
    color: var(--text-light);
    margin: 0;
  }
  .company-name {
    position: absolute;
    left: 0;
    right: 0;
    top: 560px;
    margin: 0;
    text-align: center;
    font-family: "Tinos", "Times New Roman", serif;
    font-weight: 400;
    font-size: 50px;
    line-height: 60px;
    color: var(--text-light);
  }
  .person {
    position: absolute;
    left: 86px;
    top: 818px;
  }
  .person__name {
    margin: 0;
    font-family: "Almendra", serif;
    font-weight: 400;
    font-size: 41px;
    line-height: 44px;
    letter-spacing: 1px;
    text-transform: uppercase;
    color: var(--text-dark);
  }
  .person__title {
    margin: 0;
    font-family: "Tinos", "Times New Roman", serif;
    font-size: 24px;
    line-height: 28px;
    letter-spacing: 9px;
    text-transform: uppercase;
    color: var(--text-title);
  }
  .contact {
    position: absolute;
    left: 86px;
    top: 1005px;
    font-family: "Almendra", serif;
    font-weight: 700;
    color: var(--text-dark);
  }
  .contact__phone {
    display: flex;
    align-items: center;
    gap: 4px;
    margin: 0 0 18px;
    font-weight: 400;
    font-size: 28px;
    line-height: 32px;
  }
  .contact__icon {
    width: 16px;
    height: 14px;
  }
  .contact__line {
    margin: 0;
    font-size: 24px;
    line-height: 31px;
  }
</style>
</head>
<body>
  <main class="card">
    <div class="card__base-band"></div>

    <div class="brand-mark">
      <p class="brand-mark__name">Moberly<br>Swift<br>Solutions</p>
    </div>

    <h1 class="company-name">MOBERLY SWIFT<br>SOLUTIONS<br>LLC</h1>

    <section class="person">
      <p class="person__name">Lucia Pembrook</p>
      <p class="person__title">President</p>
    </section>

    <section class="contact">
      <p class="contact__phone">
        <svg class="contact__icon" viewBox="0 0 16 14" aria-hidden="true">
          <path d="M1 4 Q8 0 15 4 L13 6 L11 5 L11 4 Q8 3 5 4 L5 5 L3 6 Z" fill="#161616"/>
          <rect x="3" y="7" width="10" height="6" rx="1" fill="#161616"/>
        </svg>
        703-482-1947
      </p>
      <p class="contact__line">lpembrook@moberlyswiftsolutions.example</p>
      <p class="contact__line">www.moberlyswiftsolutions.example</p>
    </section>
  </main>
</body>
</html>
```